Brochure Design Project

We need a brochure for our acting school, website is
www.thestagelanternhall.com - It needs to reflect youth, vitality, and people's DREAMS coming true...colors should be red and black, but open to something new as well...the courses included should be
Players' Spark Week, Rising Talent Bundle, And The Masterclass Track

Emphasis on Players' Spark Week is the short term intensity.
Rising Talent Bundle is the benefit of getting all the tools to look for acting work.
Masterclass Track is becoming a pro, and if you are in another country, being provided with a visa to come to the U.S.

I have attached pictures and logos...I will submit the copy once there is a framework...the OLD brochure is attached as well...

Thank you...

Harold

Project Deadline Extended
Reason: We would like to see a couple more ideas...

Project Deadline Extended
Reason: HI there designers! Thanks for your submissions. We are almost ready to pick a design. Thanks for the understanding.

Target Market(s)

18-35 year olds...fairly affluent, educated, American, European, or Australian

Industry/Entity Type

School

Requirements
Must have
• Make it fun, clean, clear, and NOT corporate.

```html
<!DOCTYPE html>
<html lang="en">
<head>
<meta charset="utf-8">
<title>Lantern Hall – Course Brochure</title>
<link rel="stylesheet" href="https://fonts.googleapis.com/css2?family=Open+Sans:wght@300;400;600;700;800&display=swap">
<style>
  :root {
    --stage: #2e2e2e;
    --paper: #ffffff;
    --ink: #0d0d0d;
    --slate: #4b4b4d;
    --crimson: #8f1c22;
    --crimson-deep: #7a151a;
    --wine: #6c1115;
    --text-light: #f2f2f2;
    --text-soft: #e6c9c9;
  }
  * { box-sizing: border-box; margin: 0; padding: 0; }
  html, body {
    width: 1200px; height: 793px; overflow: hidden;
    background: var(--stage);
    font-family: "Open Sans", Arial, sans-serif;
  }
  .spread {
    position: absolute; left: 60px; top: 50px;
    width: 1080px; height: 693px;
    background: var(--paper);
    overflow: hidden;
  }
  .block { position: absolute; }

  /* left page photos */
  .photo-panel { background: linear-gradient(135deg, #1a1a1a, #3a2a24 55%, #0e0e0e); }
  .photo-panel--bootcamp { left: 0; top: 0; width: 530px; height: 320px; }
  .photo-panel--bundle { left: 0; top: 326px; width: 530px; height: 290px;
    background: linear-gradient(160deg, #2a2a2a, #4a4440 50%, #121212); }
  .photo-fill { position: absolute; inset: 0; }
  .page-band { left: 0; top: 624px; width: 530px; height: 69px; background: var(--crimson); }

  .course-title {
    position: absolute; left: 26px; top: 22px;
    color: var(--paper); font-weight: 800; font-size: 14px; letter-spacing: .3px;
    text-transform: uppercase;
  }
  .course-mark {
    position: absolute; right: 22px; bottom: 18px;
    display: flex; align-items: center; gap: 6px;
    color: var(--paper); font-weight: 700; font-size: 11px; text-transform: uppercase;
  }
  .course-mark .dot { width: 10px; height: 10px; background: var(--paper); border-radius: 50%; }

  .photo-caption { position: absolute; left: 26px; color: var(--paper); }
  .photo-caption h3 { font-weight: 300; font-size: 19px; line-height: 1; text-transform: uppercase; }
  .photo-caption p { font-size: 11px; line-height: 1.3; }
  .photo-caption b { font-weight: 700; }
  .photo-caption--bootcamp { bottom: 22px; }
  .photo-caption--bundle { bottom: 8px; }
  .photo-caption--bundle h3 + p { margin-bottom: 2px; }

  /* middle column */
  .creed { left: 530px; top: 0; width: 270px; height: 320px; background: var(--slate);
    padding: 18px 16px 0 18px; color: var(--text-light); }
  .creed li { list-style: none; font-size: 7.4px; line-height: 1.32; margin-bottom: 6px; }
  .creed li b { font-weight: 700; }
  .creed-gap { left: 530px; top: 320px; width: 270px; height: 6px; background: var(--paper); }

  .bundle-info { left: 530px; top: 326px; width: 270px; height: 367px;
    background: linear-gradient(180deg, var(--crimson) 0%, var(--crimson-deep) 100%);
    padding: 16px 16px 0 18px; color: var(--text-light); }
  .bundle-info .intro { font-size: 7.4px; line-height: 1.38; margin-bottom: 8px; }

  .section-head { font-weight: 300; font-size: 15px; text-transform: uppercase; color: var(--paper); margin-top: 12px; line-height: 1.1; }
  .section-sub { font-size: 9.5px; color: var(--paper); margin-bottom: 3px; }
  .module-list li { list-style: none; font-size: 7.4px; line-height: 1.9; text-transform: uppercase; color: var(--text-soft); }
  .module-list li::before { content: "- "; }

  /* right column */
  .column-gap { left: 800px; top: 0; width: 6px; height: 693px; background: var(--paper); }
  .masterclass { left: 806px; top: 0; width: 274px; height: 693px;
    background: linear-gradient(180deg, var(--crimson-deep), var(--wine));
    padding: 0 18px 0 20px; color: var(--text-light); }
  .masterclass-photo { position: relative; margin: 22px 0 0 0; width: 236px; height: 262px;
    background: linear-gradient(150deg, #2b2523, #141414 60%, #080808); }
  .program-name { position: absolute; left: 12px; bottom: 14px; display: flex; align-items: center; gap: 8px;
    color: var(--paper); font-weight: 300; font-size: 16px; text-transform: uppercase; line-height: 1.05; }
  .program-name .dot { width: 16px; height: 16px; border-radius: 50%; background: var(--paper); flex: none; }
  .program-name small { display: block; font-size: 9px; }

  .advanced-head { display: flex; align-items: center; gap: 8px; margin-top: 14px;
    font-weight: 300; font-size: 15px; color: var(--paper); text-transform: uppercase; }
  .advanced-head .square { width: 18px; height: 18px; background: var(--crimson); border: 0; outline: 2px solid var(--paper); }
</style>
</head>
<body>
<main class="spread">

  <section class="block photo-panel photo-panel--bootcamp">
    <div class="photo-fill" role="img" aria-label="Two young actors face each other in a scene rehearsal on a dark stage, classmates watching behind"></div>
    <h2 class="course-title">Players' Spark Week</h2>
    <div class="photo-caption photo-caption--bootcamp">
      <h3>Basic Training</h3>
      <p><b>Morning Sessions:</b> 4 weeks - 5 days a week</p>
      <p><b>Evening Sessions:</b> 6 weeks - 3 nights a week</p>
    </div>
    <div class="course-mark"><span class="dot"></span>Players' Spark Week</div>
  </section>

  <section class="block photo-panel photo-panel--bundle">
    <div class="photo-fill" role="img" aria-label="Students film a scene with handheld video cameras in a black studio"></div>
    <h2 class="course-title">The Rising Talent Bundle</h2>
    <div class="photo-caption photo-caption--bundle">
      <h3>Basic Training</h3>
      <p>4 weeks / 20 hours per week</p>
      <h3>Into Battle</h3>
      <p>8 weeks / 20 hours per week</p>
    </div>
    <div class="course-mark"><span class="dot"></span>Players' Spark Week I+II</div>
  </section>

  <div class="block page-band"></div>

  <section class="block creed">
    <ul>
      <li>-All Lantern Hall actors come to class prepared and on time.</li>
      <li>-We don't charge you an arm and a leg, and a foot.</li>
      <li>-<b>All Lantern Hall teachers are currently working actors</b> with real credits, not just fancy degrees. Like all professionals we do it often and for money.</li>
      <li>-<b>We do not worship dead acting teachers</b> who were popular decades ago. Craft moves on, and so do we. We teach what works on set today, no matter whose name is on it.</li>
      <li>-<b>Our approach is uniform, practical, and current,</b> focusing on giving you all the tools you need to get a job.</li>
      <li>-<b>Our instructors have actually ACTED, and for money.</b> They don't just represent actors, or meet with actors at a party.</li>
      <li>-<b>Our students do not teach our classes.</b> They would like to, but we tell them to go out and look for acting work instead.</li>
      <li>-<b>We keep classes small,</b> to an average of 16, not 30 or 40, so that you can actually work extensively in every class.</li>
      <li>-<b>Though he wouldn't mind it,</b> we don't encourage you to worship our Artistic Director Harold Vance. We showcase your talent so that you can earn your own credits.</li>
      <li>-<b>We answer our phone and try to help you.</b> We are here to serve your need for a creative life and an acting career. Just call us, you'll see.</li>
    </ul>
  </section>
  <div class="block creed-gap"></div>

  <section class="block bundle-info">
    <p class="intro">There are those who come to Hollywood, manage to get an audition, go in hoping for the best, and fail miserably. While there is something to be said for that kind of moxie, there's also something to be said for not burning bridges. Meaning you only get one shot at a relationship with a casting director, director, or producer. So give it your best.</p>
    <p class="intro">The Rising Talent Bundle, Spark Week I and II back to back, giving you everything you need to book the part, and adding a personalized way to market yourself. It will leave you with one thing: NO EXCUSES. So what are you waiting for?</p>
    <h3 class="section-head">Basic Training</h3>
    <ul class="module-list">
      <li>Lantern Hall Technique</li>
      <li>Scene Study</li>
      <li>Cold Reading</li>
      <li>The Actor's Instrument</li>
      <li>The Daily Acting Workout</li>
    </ul>
    <h3 class="section-head">Into Battle</h3>
    <ul class="module-list">
      <li>Cold Reading/Scene Study</li>
      <li>Lantern Hall Technique</li>
      <li>Business of Show Business</li>
      <li>On Camera Technique</li>
      <li>The Daily Acting Workout</li>
    </ul>
  </section>

  <div class="block column-gap"></div>

  <section class="block masterclass">
    <div class="masterclass-photo" role="img" aria-label="The artistic director seated in an empty theatre auditorium">
      <div class="program-name"><span class="dot"></span><span><small>The</small>Masterclass Track</span></div>
    </div>
    <h3 class="section-head">Basic Training</h3>
    <p class="section-sub">4 weeks / 20 hours per week</p>
    <ul class="module-list">
      <li>Lantern Hall Technique</li>
      <li>Scene Study</li>
      <li>Cold Reading</li>
      <li>The Actor's Instrument</li>
      <li>The Daily Acting Workout</li>
    </ul>
    <h3 class="section-head">Into Battle</h3>
    <p class="section-sub">26 weeks / 572 total hours</p>
    <ul class="module-list">
      <li>Cold Reading/Scene Study</li>
      <li>Lantern Hall Technique</li>
      <li>Business of Show Business</li>
      <li>On Camera Technique</li>
      <li>The Daily Acting Workout</li>
    </ul>
    <div class="advanced-head"><span class="square"></span>Advanced Track &amp; Showcase</div>
    <p class="section-sub">26 weeks / 572 total hours</p>
    <ul class="module-list">
      <li>Advanced Scene Study/Cold Reading</li>
      <li>The Works in Progress Evening</li>
      <li>Advanced Lantern Hall Technique</li>
      <li>The Daily Acting Workout</li>
    </ul>
  </section>

</main>
</body>
</html>
```